Packaging design for Organic Beard Care brand - Talon Meadows

This packaging design will be for our beard oil collection which include five different beard oil scents and our signature blend beard oil which is separate from the collection.
There will be two different variants of the box design needed:
Variant 1: White box with Logo and text (Ingredients, Directions, etc).
The words “Handcrafted Premium Beard Oil” will be printed in green foil color. Work this into the design.
Variant 2: Black box with gold foil logo and gold foil text (Ingredients, Directions, etc).
The words “Handcrafted Premium Beard Oil” will be printed in gold foil color. Work this into the design.
Both boxes should have a premium look and feel to it without too much noise.
(Think Brisk deodorant & shampoo brand or Plume teeth whitening brand)
Key callouts will be provided to add to the box designs.
I’ve attached icons, logos, images of the beard oil products and UPC codes that should be used on each box variant.
Please message me if there are more image assets or questions you have about creating the package design.
**Important** - You must create the design on the template file: 30ml-cardboard-box-template-talon-meadows.ai. Any submissions without the design within this template will be passed up/rejected.
Men 21-50
Health & Beauty Cosmetics
- Miso, ASAP Condensed

```html
<!DOCTYPE html>
<html lang="en">
<head>
<meta charset="utf-8">
<title>Talon Meadows – Sweet Almond Beard Oil Box Panels</title>
<link rel="stylesheet" href="https://fonts.googleapis.com/css2?family=Asap+Condensed:wght@300;400;500;600;700&family=Montserrat:wght@700&display=swap">
<style>
  :root {
    --backdrop: #cbcbcb;
    --panel: #ffffff;
    --panel-edge: #ececec;
    --ink: #2a2a2a;
    --ink-soft: #444444;
    --rule: #3a3a3a;
    --bar: #231f20;
    --green-deep: #1f6b12;
    --green-mid: #3f9a1f;
    --green-light: #8fd14f;
    --foil: linear-gradient(180deg, #2b7a16 0%, #7cc63e 45%, #2a7d18 70%, #1c5e0f 100%);
    --label-ink: #111111;
  }
  * { margin: 0; padding: 0; box-sizing: border-box; }
  html, body { width: 1200px; height: 950px; overflow: hidden; }
  body {
    background: var(--backdrop);
    font-family: "Asap Condensed", "Arial Narrow", sans-serif;
    color: var(--ink);
    position: relative;
  }
  .panel {
    position: absolute;
    background: var(--panel);
    box-shadow: 6px 8px 18px rgba(0,0,0,0.18);
  }
  .panel > * { position: absolute; }
  .panel-label {
    position: absolute;
    top: 832px;
    width: 260px;
    text-align: center;
    font-family: "Montserrat", sans-serif;
    font-weight: 700;
    font-size: 21px;
    color: var(--label-ink);
  }
  .vertical { writing-mode: vertical-rl; transform: rotate(180deg); }
  .foil-text {
    background: var(--foil);
    -webkit-background-clip: text;
    background-clip: text;
    color: transparent;
  }
  .brand-mark {
    width: 100%;
    display: flex; flex-direction: column; align-items: center;
  }
  .brand-mark .dot {
    width: 30px; height: 30px; border-radius: 50%;
    background: var(--ink);
  }
  .brand-mark .name {
    margin-top: 8px;
    font-size: 14px; font-weight: 400; color: var(--ink);
  }

  /* Front option */
  .front-option { left: 82px; top: 79px; width: 247px; height: 707px; }
  .front-option .side-title {
    left: 8px; top: 84px; width: 18px; height: 543px;
    display: flex; align-items: center; gap: 8px;
    font-size: 15px; letter-spacing: 6.5px; color: var(--green-mid);
    font-weight: 400;
  }
  .front-option .side-title::before,
  .front-option .side-title::after {
    content: ""; flex: 1; width: 1.5px; background: var(--green-mid);
  }
  .front-option .big-title {
    left: 28px; top: 112px; width: 62px; height: 486px;
    font-size: 60px; font-weight: 600; letter-spacing: 17px;
    line-height: 62px; text-align: center;
  }
  .front-option .divider {
    left: 92px; top: 84px; width: 2px; height: 543px;
    background: var(--green-deep);
  }
  .front-option .brand-mark { left: 92px; top: 104px; width: 155px; }
  .front-option .flavour-band {
    left: 92px; top: 181px; width: 155px; height: 37px;
    background: linear-gradient(90deg, var(--green-deep), var(--green-light) 55%, var(--green-deep));
    color: #fff; font-size: 17px; letter-spacing: 2px; font-weight: 300;
    display: flex; align-items: center; justify-content: center;
  }
  .front-option .claim {
    left: 92px; top: 230px; width: 155px;
    text-align: center; font-size: 11px; line-height: 19px;
    letter-spacing: 0.5px; color: var(--ink-soft); text-transform: uppercase;
  }
  .front-option .claim-rule {
    left: 92px; top: 276px; width: 155px; height: 1px; background: var(--rule);
  }
  .front-option .aside {
    left: 92px; top: 282px; width: 155px;
    text-align: center; font-size: 11px; color: var(--ink-soft);
  }
  .front-option .net-weight {
    left: 92px; top: 600px; width: 155px;
    text-align: center; font-size: 12px; color: var(--ink-soft);
  }

  /* Copy panels shared */
  .section-heading {
    font-size: 17px; font-weight: 500; letter-spacing: 1px; color: var(--ink);
  }
  .section-rule { height: 1px; background: var(--rule); }
  .copy {
    font-size: 12.5px; line-height: 19px; font-weight: 300; color: var(--ink);
  }
  .copy p + p { margin-top: 19px; }

  /* Side panel 1 */
  .side-directions { left: 353px; top: 79px; width: 243px; height: 707px; }
  .side-directions .directions-heading { left: 19px; top: 190px; }
  .side-directions .directions-rule { left: 12px; top: 216px; width: 223px; }
  .side-directions .directions-copy { left: 19px; top: 232px; width: 205px; }
  .side-directions .ingredients-heading { left: 19px; top: 480px; }
  .side-directions .ingredients-rule { left: 12px; top: 505px; width: 223px; }
  .side-directions .ingredients-copy { left: 19px; top: 521px; width: 205px; }

  /* Front */
  .front { left: 637px; top: 84px; width: 246px; height: 712px; }
  .front .flavour {
    left: 0; top: 58px; width: 100%; text-align: center;
    font-size: 20px; font-weight: 400; letter-spacing: 5px; color: var(--ink);
  }
  .front .claim {
    left: 0; top: 102px; width: 100%; text-align: center;
    font-size: 11px; letter-spacing: 0.3px; color: var(--ink-soft);
  }
  .front .aside {
    left: 0; top: 121px; width: 100%; text-align: center;
    font-size: 10px; letter-spacing: 0.4px; color: var(--ink-soft);
    text-transform: uppercase;
  }
  .front .title-word {
    left: 78px; top: 200px; width: 64px; height: 310px;
    font-size: 72px; font-weight: 700; letter-spacing: 14px;
    line-height: 64px; text-align: center;
  }
  .front .title-sub {
    left: 160px; top: 209px; width: 34px; height: 298px;
    display: flex; align-items: center; gap: 16px;
    font-size: 34px; font-weight: 300; letter-spacing: 16px; line-height: 34px;
    color: var(--green-mid);
  }
  .front .title-sub::before,
  .front .title-sub::after {
    content: ""; flex: 1; width: 2px; background: var(--green-mid);
  }
  .front .premium-bar {
    left: 4px; top: 569px; width: 233px; height: 24px;
    background: var(--bar); color: #fff;
    font-size: 15px; letter-spacing: 0.5px; font-weight: 400;
    display: flex; align-items: center; justify-content: center;
  }
  .front .net-weight {
    left: 0; top: 631px; width: 100%; text-align: center;
    font-size: 12px; color: var(--ink-soft);
  }

  /* Side panel 2 */
  .side-story { left: 904px; top: 82px; width: 246px; height: 711px; }
  .side-story .brand-mark { left: 0; top: 56px; }
  .side-story .brand-mark .dot { width: 26px; height: 26px; }
  .side-story .brand-mark .name { font-size: 10px; margin-top: 5px; }
  .side-story .kicker {
    left: 50px; top: 114px; width: 146px;
    display: flex; align-items: center; gap: 5px;
    font-size: 8px; letter-spacing: 0.6px; color: var(--ink); font-weight: 500;
  }
  .side-story .kicker::before,
  .side-story .kicker::after { content: ""; flex: 1; height: 1px; background: var(--ink); }
  .side-story .product-name {
    left: 0; top: 124px; width: 100%; text-align: center;
    font-size: 36px; font-weight: 600; letter-spacing: -0.5px; color: #111;
  }
  .side-story .story-copy { left: 23px; top: 186px; width: 205px; }
  .side-story .story-rule { left: 19px; top: 571px; width: 219px; }
  .side-story .motto {
    left: 23px; top: 594px; width: 210px;
    font-size: 12.5px; line-height: 19px; font-weight: 300; text-transform: uppercase;
  }
</style>
</head>
<body>

  <section class="panel front-option">
    <div class="side-title vertical">HANDCRAFTED PREMIUM</div>
    <div class="big-title vertical foil-text">BEARD OIL</div>
    <div class="divider"></div>
    <div class="brand-mark"><span class="dot"></span><span class="name">Talon Meadows</span></div>
    <div class="flavour-band">SWEET ALMOND</div>
    <div class="claim">100% All-Natural<br>&amp; Organic Ingredients</div>
    <div class="claim-rule"></div>
    <div class="aside">None of that artificial stuff!</div>
    <div class="net-weight">net wt. 30ml / 1 fl. oz.</div>
  </section>

  <section class="panel side-directions">
    <h2 class="section-heading directions-heading">DIRECTIONS</h2>
    <div class="section-rule directions-rule"></div>
    <div class="copy directions-copy">
      <p>Squeeze 1–2 pulls of oil to the palm of your hand. For longer beards,<br>use 3–4 pulls of oil.</p>
      <p>Rub hands together and massage into beard. Finish by styling as usual with a beard comb or pick to spread beard oil evenly throughout your beard.</p>
      <p>Use daily for best results.</p>
    </div>
    <h2 class="section-heading ingredients-heading">INGREDIENTS</h2>
    <div class="section-rule ingredients-rule"></div>
    <div class="copy ingredients-copy">
      <p>Castor Oil, Avocado Oil, Grapeseed Oil, Vitamin E, Sweet Almond Oil</p>
    </div>
  </section>

  <section class="panel front">
    <div class="flavour">SWEET ALMOND</div>
    <div class="claim">100% ALL-NATURAL &amp; ORGANIC INGREDIENTS</div>
    <div class="aside">None of that artificial stuff!</div>
    <div class="title-word vertical foil-text">BEARD</div>
    <div class="title-sub vertical">OIL</div>
    <div class="premium-bar">HANDCRAFTED PREMIUM</div>
    <div class="net-weight">net wt. 30ml / 1 fl. oz.</div>
  </section>

  <section class="panel side-story">
    <div class="brand-mark"><span class="dot"></span><span class="name">Talon Meadows</span></div>
    <div class="kicker">HANDCRAFTED PREMIUM</div>
    <h1 class="product-name">BEARD OIL</h1>
    <div class="copy story-copy">
      <p>Talon Meadows was created out of a necessity to provide beard oils that are made with natural and organic ingredients that would not be harmful to men who have skin sensitivities to heavy fragrances and artificial fillers.</p>
      <p>We have helped thousands of men keep their beards healthy and smelling good for over half a decade with amazing products and solid education on the many types of oils and ingredients that go into our beard oils and other beard care products.</p>
      <p>Our beard oils have been proven to prevent beard itch and beard dandruff while keeping your beard feeling soft and manageable everyday.</p>
    </div>
    <div class="section-rule story-rule"></div>
    <div class="motto">Quality ingredients. Quality service. Everyday.</div>
  </section>

  <div class="panel-label" style="left:76px">FRONT OPTION</div>
  <div class="panel-label" style="left:345px">SIDE PANEL 1</div>
  <div class="panel-label" style="left:630px">FRONT</div>
  <div class="panel-label" style="left:897px">SIDE PANEL 2</div>

</body>
</html>
```